A clean crisp business card for a Landscape Construction company. Designed to be easy to read contact/ info and also be appealing/interesting, unlike a traditional business card.

Industry/Entity Type

Landscape Construction

Contact Information for Business Card

Company name : Bramblecrest Landscape Construction, phone number: (877) 62Vales, website:Bramblecrestlandscapes.example, Email, sales@bramblecrestlandscapes.example

Requirements
Nice to have
• Luxurious finishes/ details…. Icons or emblems next to contact info
Should not have
• Clipart or general pictures

```html
<!DOCTYPE html>
<html lang="en">
<head>
<meta charset="utf-8">
<title>Bramblecrest Landscape Construction – Business Card</title>
<link rel="stylesheet" href="https://fonts.googleapis.com/css2?family=Josefin+Sans:wght@400;600;700&display=swap">
<style>
  :root {
    --leaf-green: #9dc63b;
    --river-blue: #2468b4;
    --card-black: #030303;
    --ink-white: #ffffff;
    --backdrop: #efefef;
  }
  * { box-sizing: border-box; margin: 0; padding: 0; }
  html, body {
    width: 1200px; height: 1000px; overflow: hidden;
    background: var(--backdrop);
    font-family: "Josefin Sans", sans-serif;
  }
  .card-sheet {
    position: relative; width: 1200px; height: 1000px;
  }
  .card {
    position: absolute; top: 345px;
    width: 540px; height: 309px;
    background: var(--card-black);
    overflow: hidden;
    box-shadow: 0 2px 6px rgba(0,0,0,.15);
  }
  .card--front { left: 40px; }
  .card--back { left: 620px; }
  .card__waves { position: absolute; inset: 0; width: 100%; height: 100%; }
  .wave--green { fill: var(--leaf-green); }
  .wave--blue { fill: var(--river-blue); }

  .front__title {
    position: absolute; left: 157px; top: 38px;
    color: var(--ink-white);
  }
  .front__name {
    font-size: 23px; font-weight: 700; letter-spacing: 1.5px; line-height: 1;
  }
  .front__tagline {
    font-size: 12.5px; font-weight: 400; letter-spacing: 1.3px; margin-top: 4px;
  }
  .contact-list {
    position: absolute; left: 200px; top: 183px; list-style: none;
  }
  .contact-list__item {
    display: flex; align-items: center; height: 34px;
    color: var(--ink-white); font-size: 14.5px; letter-spacing: .3px;
  }
  .contact-list__icon {
    width: 24px; height: 24px; margin-right: 16px; flex: none;
  }
  .contact-list__icon circle.ring { fill: none; stroke: var(--leaf-green); stroke-width: 1.6; }
  .contact-list__icon .glyph { fill: none; stroke: var(--leaf-green); stroke-width: 1.5; stroke-linecap: round; stroke-linejoin: round; }

  .brand-mark {
    position: absolute; text-align: center;
    color: var(--river-blue); font-weight: 600;
  }
  .brand-mark__dot {
    display: block; margin: 0 auto 6px; border-radius: 50%;
    background: var(--leaf-green);
  }
  .brand-mark--small { left: 16px; top: 196px; width: 170px; }
  .brand-mark--small .brand-mark__dot { width: 26px; height: 26px; }
  .brand-mark--small .brand-mark__name { font-size: 17px; letter-spacing: .5px; line-height: 1; }
  .brand-mark--small .brand-mark__sub { font-size: 8.5px; letter-spacing: .8px; margin-top: 3px; }

  .brand-mark--large { left: 0; right: 0; top: 95px; }
  .brand-mark--large .brand-mark__dot { width: 44px; height: 44px; margin-bottom: 10px; }
  .brand-mark--large .brand-mark__name { font-size: 36px; letter-spacing: 1px; line-height: 1; }
  .brand-mark--large .brand-mark__sub { font-size: 13px; letter-spacing: 2px; margin-top: 5px; }
</style>
</head>
<body>
<main class="card-sheet">

  <section class="card card--front" aria-label="Business card front">
    <svg class="card__waves" viewBox="0 0 453 259" preserveAspectRatio="none" aria-hidden="true">
      <path class="wave--blue" d="M0,0 H453 V48 C380,58 300,100 200,117 C120,128 50,95 0,42 Z"/>
      <path class="wave--green" d="M0,0 H453 V40 C380,48 300,82 200,97 C120,108 50,80 0,36 Z"/>
    </svg>

    <div class="front__title">
      <div class="front__name">BRAMBLECREST</div>
      <div class="front__tagline">LANDSCAPE CONSTRUCTION</div>
    </div>

    <div class="brand-mark brand-mark--small">
      <span class="brand-mark__dot"></span>
      <div class="brand-mark__name">BRAMBLECREST</div>
      <div class="brand-mark__sub">LANDSCAPE CONSTRUCTION</div>
    </div>

    <ul class="contact-list">
      <li class="contact-list__item">
        <svg class="contact-list__icon" viewBox="0 0 24 24" aria-hidden="true">
          <circle class="ring" cx="12" cy="12" r="11"/>
          <path class="glyph" d="M8.5,7 l2,0 l1,3 l-1.3,1 c.7,1.5 1.7,2.5 3.2,3.2 l1-1.3 l3,1 l0,2 c-5,.5 -9.5,-4 -8.9,-8.9 z"/>
        </svg>
        (877) 62Vales
      </li>
      <li class="contact-list__item">
        <svg class="contact-list__icon" viewBox="0 0 24 24" aria-hidden="true">
          <circle class="ring" cx="12" cy="12" r="11"/>
          <rect class="glyph" x="6.5" y="8" width="11" height="8" rx="1"/>
          <path class="glyph" d="M6.5,8.5 L12,12.5 L17.5,8.5"/>
        </svg>
        bramblecrestlandscapes.example
      </li>
      <li class="contact-list__item">
        <svg class="contact-list__icon" viewBox="0 0 24 24" aria-hidden="true">
          <circle class="ring" cx="12" cy="12" r="11"/>
          <circle class="glyph" cx="12" cy="12" r="6"/>
          <ellipse class="glyph" cx="12" cy="12" rx="2.6" ry="6"/>
          <path class="glyph" d="M6,12 H18 M7,9 H17 M7,15 H17"/>
        </svg>
        sales@bramblecrestlandscapes.example
      </li>
    </ul>
  </section>

  <section class="card card--back" aria-label="Business card back">
    <svg class="card__waves" viewBox="0 0 453 259" preserveAspectRatio="none" aria-hidden="true">
      <path class="wave--blue" d="M0,0 H453 C400,12 300,30 180,45 C100,55 40,52 0,34 Z"/>
      <path class="wave--green" d="M0,0 H453 C400,8 300,20 180,32 C100,40 40,38 0,14 Z"/>
      <path class="wave--blue" d="M0,259 C80,240 150,205 230,198 C320,190 390,195 453,210 V259 Z"/>
      <path class="wave--green" d="M0,259 C100,250 170,215 240,208 C320,200 390,205 453,218 V259 Z"/>
    </svg>

    <div class="brand-mark brand-mark--large">
      <span class="brand-mark__dot"></span>
      <div class="brand-mark__name">BRAMBLECREST</div>
      <div class="brand-mark__sub">LANDSCAPE CONSTRUCTION</div>
    </div>
  </section>

</main>
</body>
</html>
```